Banners for Affiliate Marketing on Tantra website

We are starting an affiliate marketing program on our website brightmeadowhub.com and need banner ads for our affiliates. We are looking for the following sizes

for sure: 728x90, 300x250, 160x600
possibly: 468x60, 250x250, 125x125

Banner ads should market a several of our products - online tantra store, various tantra workshops, tantra vacations. See our website for details on what we offer.

For example, EITHER we may need one banner ad each in different sizes for:

Women's Workshop
Tantra Vacations
Tantric Massage workshop
Golden Hearth workshop
Joy & Harmony Course
Selected products from our store, for example Gentle Touch for Partners DVD, or Wendel Bundle

OR maybe we just need one banner ad in all the sizes for
Workshops
Store
Vacations

All images on our site can be used, or use other stock images.

The winner of this project will continue to work with us on graphic design of future banners, and we are also looking for a logo design.

Target Market(s)

couples, singles, age group 28-65, with disposable income

Industry/Entity Type

Graphic Design

Requirements
Must have
• Modern, attractive design that matches the branding and coloring on our website.
Should not have
• no obvious nudity in any graphics

```html
<!DOCTYPE html>
<html lang="en">
<head>
<meta charset="utf-8">
<title>Bright Meadow Institute – Affiliate Banners</title>
<link rel="stylesheet" href="https://fonts.googleapis.com/css2?family=Cinzel:wght@400;500&display=swap">
<style>
  :root {
    --canvas: #111111;
    --sand: #d8ccb0;
    --crimson: #b0182b;
    --crimson-light: #c8273a;
    --crimson-dark: #8e0f20;
    --ivory: #fbf5ea;
    --brand-red: #a8192c;
  }
  * { box-sizing: border-box; margin: 0; padding: 0; }
  html, body {
    width: 1200px; height: 812px; overflow: hidden;
    background: var(--canvas);
    font-family: "Cinzel", "Trajan Pro", serif;
  }
  .canvas { position: relative; width: 1200px; height: 812px; }

  .banner { position: absolute; overflow: hidden; display: flex; }
  .banner--skyscraper { left: 42px; top: 37px; width: 197px; height: 741px; flex-direction: column; }
  .banner--leaderboard { left: 261px; top: 239px; width: 902px; height: 111px; flex-direction: row; }
  .banner--rectangle { left: 261px; top: 371px; width: 372px; height: 309px; flex-direction: column; }

  .brand {
    background: var(--sand);
    display: flex; align-items: center; justify-content: center;
    color: var(--brand-red); text-align: center; font-weight: 400;
    line-height: 1.2;
  }
  .banner--skyscraper .brand { height: 147px; font-size: 20px; padding-top: 40px; }
  .banner--leaderboard .brand { width: 187px; font-size: 17px; padding-top: 26px; }
  .banner--rectangle .brand { height: 70px; font-size: 17px; padding-left: 40px; }

  .offer {
    background: radial-gradient(ellipse at 55% 45%, var(--crimson-light) 0%, var(--crimson) 45%, var(--crimson-dark) 100%);
    color: var(--ivory);
    display: flex; flex-direction: column; align-items: center; justify-content: center;
    text-align: center; font-weight: 400;
    text-shadow: 0 1px 2px rgba(60, 0, 10, 0.45);
  }
  .offer__line { display: block; line-height: 1.1; }
  .offer__rule {
    display: block; height: 1px; width: 70%;
    background: linear-gradient(90deg, transparent, rgba(255,235,220,0.55), transparent);
    margin: 6px 0;
  }
  .banner--skyscraper .offer { height: 233px; font-size: 27px; }
  .banner--skyscraper .offer__rule { margin: 10px 0; }
  .banner--leaderboard .offer { width: 373px; font-size: 28px; }
  .banner--rectangle .offer { height: 124px; font-size: 28px; }

  .photo { flex: 1; position: relative; }
  .photo--beach {
    background: linear-gradient(180deg, #7fc3cf 0%, #9fd2d6 32%, #c8b8a6 55%, #e6ddd0 75%, #efe9e0 100%);
  }
  .photo--group {
    background: linear-gradient(90deg, #6f8a4a 0%, #c59a7c 22%, #d8b49a 45%, #a88b6c 65%, #8aa0a6 85%, #b9a988 100%);
  }
  .photo--couple {
    background: linear-gradient(90deg, #f4efe6 0%, #e2c2a6 30%, #d9b399 55%, #c9a08a 75%, #efe9e2 100%);
  }

  .cta {
    position: absolute;
    display: flex; flex-direction: column; align-items: center; justify-content: center;
    color: var(--ivory); text-align: center; line-height: 1.15;
  }
  .cta svg { position: absolute; inset: 0; }
  .cta__label { position: relative; }
  .banner--skyscraper .cta { left: 30px; top: 602px; width: 128px; height: 128px; font-size: 24px; }
  .banner--leaderboard .cta { left: 798px; top: 8px; width: 98px; height: 98px; font-size: 18px; }
</style>
</head>
<body>
<main class="canvas">

  <section class="banner banner--skyscraper" aria-label="160 by 600 banner">
    <div class="brand">Bright Meadow<br>Institute</div>
    <div class="offer">
      <span class="offer__line">Tantra</span>
      <span class="offer__line">Workshops</span>
      <span class="offer__rule"></span>
      <span class="offer__line">Store</span>
      <span class="offer__rule"></span>
      <span class="offer__line">Vacations</span>
    </div>
    <div class="photo photo--beach" role="img" aria-label="Photo of a couple sitting together on a tropical beach"></div>
    <a class="cta" href="#">
      <svg viewBox="0 0 100 100" aria-hidden="true">
        <defs>
          <radialGradient id="sealSky" cx="45%" cy="40%" r="60%">
            <stop offset="0" stop-color="#c8273a"/>
            <stop offset="1" stop-color="#8e0f20"/>
          </radialGradient>
        </defs>
        <circle cx="50" cy="50" r="49" fill="url(#sealSky)"/>
        <circle cx="50" cy="50" r="43" fill="none" stroke="#d94a5a" stroke-width="0.8"/>
      </svg>
      <span class="cta__label">Learn<br>More</span>
    </a>
  </section>

  <section class="banner banner--leaderboard" aria-label="728 by 90 banner">
    <div class="brand">Bright Meadow<br>Institute</div>
    <div class="offer">
      <span class="offer__line">Tantra Workshops</span>
      <span class="offer__rule"></span>
      <span class="offer__line">Store &amp; Vacation</span>
    </div>
    <div class="photo photo--group" role="img" aria-label="Photo of a smiling group of workshop participants outdoors"></div>
    <a class="cta" href="#">
      <svg viewBox="0 0 100 100" aria-hidden="true">
        <defs>
          <radialGradient id="sealLeader" cx="45%" cy="40%" r="60%">
            <stop offset="0" stop-color="#c8273a"/>
            <stop offset="1" stop-color="#8e0f20"/>
          </radialGradient>
        </defs>
        <circle cx="50" cy="50" r="49" fill="url(#sealLeader)"/>
        <circle cx="50" cy="50" r="43" fill="none" stroke="#d94a5a" stroke-width="0.8"/>
      </svg>
      <span class="cta__label">Learn<br>More</span>
    </a>
  </section>

  <section class="banner banner--rectangle" aria-label="300 by 250 banner">
    <div class="brand">Bright Meadow Institute</div>
    <div class="offer">
      <span class="offer__line">Tantra Workshops</span>
      <span class="offer__rule"></span>
      <span class="offer__line">Store &amp; Vacation</span>
    </div>
    <div class="photo photo--couple" role="img" aria-label="Close-up photo of a mature couple leaning their foreheads together"></div>
  </section>

</main>
</body>
</html>
```